Custom Header Designs - Automotive Parts - Alternator & Starter

We need 8 Header/Hero designs that will be used on our website. We are a company based in Montreal Canada and we re-manufacture Alternators and Starters for all types of vehicles. We offer a premium product and we are looking for premium designs that reflect the look of our packaging and the look of our website. Essentially we specialize in the sale and manufacture of two specific parts that go on all types of vehicles, Alternators and Starters. All text on these designs need to be editable as we will need to translate them to French once we get the source files.
Here are some websites of our competitors so you can draw some inspiration and see what our industry/business is all about:
https://www.qelvorparts.com/
https://www.zentrihaul.com/
Article that describes a remanufactured product, https://www.wombrixo.com/articles/starters-and-alternators-reman-vs-new.html
Our packaging is modern, sleek and professional. Our website is a B2B E-Commerce Site as well as an info site to promote our products. It is clean and minimal but we want the header/hero designs to help it stand out. Our main colors are blue and gray (as seen in our logo), but you can use whatever you like to compliment these colors.
Our packaging design was done on PixelTroupe, here is the link to that project so that you can see the packaging look and use any of the info that is from that project.
https://jobs.pixeltroupe.ca/job/5829463
The 8 Header/Hero designs will be used in the following areas, I have included a brief description of what we are looking for:
1 - Homepage Header/Hero image - This will be the homepage hero image therefore it should summarize the info described below. We offer premium quality re-manufactured alternators and starters. We are a wholesaler/distributor that services major auto-part stores with these quality products.
2 - General Product Header/Hero image - This image will be used as a header where the customer can learn general info about our products and any custom work we can do. This page will have a section where you can click to learn more about our individual product lines (links to product specific pages mentioned below) and a description of the custom work we can perform. We offer a two year manufacturers warranty.
3 - Alternator Product Header/Hero image - This image will be used to showcase our Alternator Product Line. Its purpose is to promote and advertise our premium re-manufactured alternators. This page will provide detailed info about our alternator re-manufacturing process and describe why our alternators are great.
4 - Starter Product Header/Hero image - This image will be used to showcase our Starter Product Line. Its purpose is to promote and advertise our premium re-manufactured starters. This page will provide detailed info about our starter re-manufacturing process and describe why our starters are great.
5 - General Header/Hero Image - This image will be used in most of our standard pages like our terms and conditions, privacy policy, warranty policy, our company page, etc. It needs to relate to the industry but be general enough so that we could use it in multiple areas
6 - Online Ordering Header image - This image will be used in our B2B area to introduce our customers to the Online Ordering system, its purpose is to advertise and explain some of the features of the Online Ordering system.
7 - B/O Re-Manufacture & Return Header Image - This image will be used in our B2B area to explain and advertise to our customers how our Backorder/R&R process works on our website. Essentially if we do not have the remanufactured part in stock but we have the core you could put the product on Backorder and we will remanufacture it in a few hours. If for any reason (rare vehicle, old vehicle, etc.) we do not have the core we will R&R (Remanufacture and Return) the customers core for them.
8 - Bulk Ordering Form Header Image - This image will be used in our B2B area to explain and advertise to our customers how our Bulk Ordering Form works on our website.
These hero/header images will be going on a Plankly/TillNest website and I am suggesting these images have a size of 1600 x 500, but we will take any other suggestions from the designers as you are the experts.
I have included a zip file that includes images of various elements that will help you in the design process.
Target Market(s)
Educate consumers about our products and attract auto supply chains to become distributors of our products.
Industry/Entity Type
Automotive Part

```html
<!DOCTYPE html>
<html lang="en">
<head>
<meta charset="utf-8">
<title>Ampvera – Premium Auto Parts</title>
<link rel="stylesheet" href="https://fonts.googleapis.com/css2?family=Audiowide&family=Montserrat:wght@400;700;800&display=swap">
<style>
  :root{
    --blue-deep:#0a2a6b;
    --blue-mid:#0f4fa8;
    --blue-bright:#1f7be0;
    --blue-glow:#3aa0ff;
    --white:#ffffff;
    --text-soft:#e6eefb;
    --silver-light:#f1f3f6;
    --silver-mid:#c9ced6;
    --silver-dark:#8b929c;
    --logo-blue:#0d3f95;
  }
  *{margin:0;padding:0;box-sizing:border-box;}
  html,body{width:1200px;height:375px;overflow:hidden;background:var(--blue-deep);}
  .hero{
    position:relative;width:1200px;height:375px;overflow:hidden;
    background:
      radial-gradient(ellipse 520px 300px at 700px 170px, rgba(58,160,255,.35), transparent 70%),
      linear-gradient(100deg, #0b2f78 0%, var(--blue-mid) 45%, #0d3e92 70%, #0a3588 100%);
    font-family:"Montserrat",sans-serif;
  }
  .hero__decor{position:absolute;inset:0;width:1200px;height:375px;}
  .hero__title{
    position:absolute;left:62px;top:112px;
    font-family:"Audiowide",sans-serif;font-weight:400;
    font-size:41px;line-height:50px;letter-spacing:1px;
    color:var(--white);text-transform:uppercase;
  }
  .hero__points{position:absolute;left:66px;top:221px;list-style:none;}
  .hero__point{
    display:flex;align-items:center;gap:13px;
    font-size:12.6px;color:var(--text-soft);line-height:22.5px;
  }
  .hero__point svg{width:20px;height:8px;flex:none;}
  .hero__product{
    position:absolute;left:800px;top:38px;width:334px;height:306px;
    border-radius:48% 44% 46% 42%;
    background:radial-gradient(circle at 40% 45%, var(--silver-light) 0%, var(--silver-mid) 55%, var(--silver-dark) 100%);
  }
  .hero__band{
    position:absolute;left:0;top:315px;width:1200px;height:60px;
    background:linear-gradient(90deg, #ffffff 0%, #f4f7fb 25%, rgba(220,232,248,.75) 50%, rgba(120,170,230,0) 80%);
    border-top:1px solid rgba(255,255,255,.6);
  }
  .brand{
    position:absolute;left:18px;top:332px;display:flex;align-items:center;gap:7px;
  }
  .brand__mark{width:22px;height:22px;border-radius:50%;background:var(--logo-blue);}
  .brand__name{font-weight:800;font-size:17px;color:var(--logo-blue);}
</style>
</head>
<body>
<section class="hero">
  <svg class="hero__decor" viewBox="0 0 1200 375" aria-hidden="true">
    <g class="hero__chevrons" fill="#ffffff">
      <polygon points="416,24 446,24 482,61 446,98 416,98 452,61" opacity=".16"/>
      <polygon points="466,24 496,24 532,61 496,98 466,98 502,61" opacity=".2"/>
      <polygon points="516,24 546,24 582,61 546,98 516,98 552,61" opacity=".22"/>
      <polygon points="566,24 596,24 632,61 596,98 566,98 602,61" opacity=".2"/>
      <polygon points="616,24 646,24 682,61 646,98 616,98 652,61" opacity=".16"/>
      <polygon points="666,24 696,24 732,61 696,98 666,98 702,61" opacity=".1"/>
    </g>
    <g class="hero__waves" fill="none" stroke="#6fc0ff" stroke-width="1.2" opacity=".45">
      <path d="M600 375 C760 300 900 330 1200 210"/>
      <path d="M640 375 C790 315 930 345 1200 235"/>
      <path d="M700 375 C830 330 960 360 1200 262"/>
      <path d="M0 40 C200 10 320 120 560 60"/>
    </g>
    <path d="M760 375 C900 300 1050 300 1200 250 L1200 375 Z" fill="#2b8cf0" opacity=".35"/>
  </svg>

  <h1 class="hero__title">Premium Auto Parts<br>That Keep You Running</h1>

  <ul class="hero__points">
    <li class="hero__point">
      <svg viewBox="0 0 20 8"><path d="M5 0.5 1.5 4 5 7.5M10 0.5 6.5 4 10 7.5M15 0.5 11.5 4 15 7.5" fill="none" stroke="#5fb4ff" stroke-width="1.4"/></svg>
      We offer premium quality re-manufactured alternators and starters.
    </li>
    <li class="hero__point">
      <svg viewBox="0 0 20 8"><path d="M5 0.5 1.5 4 5 7.5M10 0.5 6.5 4 10 7.5M15 0.5 11.5 4 15 7.5" fill="none" stroke="#5fb4ff" stroke-width="1.4"/></svg>
      We are a wholesaler/distributor that services major auto-part stores with these quality products.
    </li>
  </ul>

  <div class="hero__product" role="img" aria-label="Product photo of a silver remanufactured alternator with a black pulley"></div>

  <div class="hero__band"></div>
  <div class="brand">
    <span class="brand__mark"></span>
    <span class="brand__name">Ampvera</span>
  </div>
</section>
</body>
</html>
```